Brisk Refrigeration. Refrigeration and air conditioning specialists.

We need a website to promote our business. We would a modern simple design using the colours from our logo and black. We want it to be fun but proffesional.

Target Market(s)

Commercial

Number of Pages Required

4 page

Requirements
Must have
• Home Page, About Us, Services and Contact Us.
• 24/7 365 days service available.
• Brisk Refrigeration's dedicated team specialises in commercial refrigeration and air conditioning equipment.
• Based in Joondalup, we cover Perth Metro and surrounding areas.
Nice to have
• KNOWLEDGE . EXPERIENCE . PASSION in bold.
• Our experienced and highly trained technicians provide extensive knowledge and exceptional skills for your commercial refrigeration and air conditioning requirements.
• Pictures of commercial refrigeration.
Should not have
• No mention of domestic services.

```html
<!DOCTYPE html>
<html lang="en">
<head>
<meta charset="utf-8">
<title>Brisk Refrigeration</title>
<link rel="stylesheet" href="https://fonts.googleapis.com/css2?family=Montserrat:wght@400;500;600;700&family=Raleway:wght@400;500;600&family=Roboto:wght@400;500;700&display=swap">
<style>
:root{
  --purple:#41275f;
  --purple-deep:#3a2356;
  --lime:#a6ee6a;
  --lime-text:#a9e85c;
  --white:#ffffff;
  --ink:#3b2a55;
  --grey-text:#555b66;
  --line:#b9b9c2;
}
*{box-sizing:border-box;margin:0;padding:0}
html,body{width:1200px;height:3285px;overflow:hidden;background:var(--white)}
body{position:relative;font-family:'Raleway',sans-serif;color:var(--grey-text)}

/* Header */
.site-header{position:absolute;left:0;top:0;width:1200px;height:170px;background:var(--white);border-bottom:5px solid var(--lime)}
.brand-name{position:absolute;left:83px;top:50px;width:200px;font-family:'Montserrat',sans-serif;font-weight:700;font-size:30px;line-height:32px;color:var(--lime)}
.header-contact{position:absolute;top:86px;text-align:center;font-family:'Roboto',sans-serif;color:var(--ink);white-space:nowrap}
.header-contact .label{font-size:15px;color:#333}
.header-contact .value{font-size:15px;margin-top:4px}
.header-contact.call{left:300px;width:176px}
.header-contact.call .value{font-size:21px;font-weight:700;color:var(--purple)}
.header-contact.mail{left:500px;width:216px}
.header-contact.mail .value{color:var(--purple)}
.main-nav{position:absolute;left:770px;top:98px;display:flex;gap:14px;align-items:center;font-family:'Roboto',sans-serif;font-size:13px;font-weight:500;color:var(--purple);white-space:nowrap}
.main-nav .current{background:var(--lime);padding:5px 10px;border-radius:12px}

/* Hero */
.hero{position:absolute;left:0;top:175px;width:1200px;height:661px;border-bottom:5px solid var(--lime);overflow:hidden}
.hero-photo{position:absolute;inset:0;background:linear-gradient(90deg,#3a2f2a 0%,#55483e 35%,#6e6459 60%,#3d4657 75%,#2a3550 100%)}
.hero-copy{position:absolute;left:74px;top:275px;color:var(--white);font-family:'Montserrat',sans-serif;white-space:nowrap}
.hero-copy .lead{font-size:33px;font-weight:400}
.hero-copy .focus{margin-top:12px;font-size:34px;font-weight:700;line-height:42px;color:var(--lime);text-transform:uppercase}
.hero-band{position:absolute;left:0;top:434px;width:705px;height:46px;background:rgba(65,39,95,.92);color:var(--lime);font-family:'Montserrat',sans-serif;font-weight:600;font-size:28px;letter-spacing:1px;line-height:46px;padding-left:74px;white-space:nowrap;overflow:hidden}
.hero-dots{position:absolute;left:103px;top:596px;display:flex;gap:9px}
.hero-dots span{width:10px;height:10px;border-radius:50%;border:2px solid var(--white)}
.hero-dots span.on{background:var(--white)}

/* Headings */
.section-title{position:absolute;left:0;width:1200px;text-align:center;font-family:'Montserrat',sans-serif;font-weight:600;font-size:29px}
.section-title::after{content:"";display:block;width:72px;height:1px;margin:16px auto 0;background:currentColor;opacity:.5}

/* About */
.about{position:absolute;left:0;top:836px;width:1200px;height:424px}
.about .section-title{top:60px;color:var(--purple)}
.about-text{position:absolute;left:110px;width:980px;text-align:center;font-size:12.5px;line-height:22px;color:var(--grey-text)}
.pill-btn{position:absolute;left:530px;width:138px;height:34px;border-radius:17px;background:var(--purple);color:var(--white);font-family:'Roboto',sans-serif;font-size:12px;font-weight:500;line-height:34px;padding-left:26px;white-space:nowrap}
.pill-btn svg{position:absolute;right:4px;top:4px}

/* Services */
.services{position:absolute;left:0;top:1260px;width:1200px;height:1051px;background:var(--purple)}
.services .section-title{top:78px;color:var(--lime-text)}
.services-intro{position:absolute;left:80px;top:172px;width:1040px;text-align:center;font-size:12.5px;line-height:29px;color:var(--white)}
.service{position:absolute;width:236px;text-align:center}
.service-frame{width:236px;height:200px;background:var(--white);border-radius:14px;padding:14px}
.service-photo{width:100%;height:100%;border-radius:6px;background:linear-gradient(160deg,#f4f5f6,#c9ccd1)}
.service-name{margin-top:25px;font-family:'Raleway',sans-serif;font-weight:600;font-size:18px;color:var(--lime-text);white-space:nowrap}
.service-desc{margin-top:9px;font-size:12px;line-height:18px;color:var(--white)}

/* Contact */
.contact{position:absolute;left:0;top:2311px;width:1200px;height:579px}
.contact .section-title{top:56px;color:var(--purple)}
.field-label{position:absolute;font-family:'Roboto',sans-serif;font-size:13px;color:var(--purple)}
.field-label b{color:var(--purple);margin-left:6px;font-weight:400}
.field{position:absolute;border:1px solid var(--line);background:var(--white)}
.note{position:absolute;font-size:13px;color:var(--purple)}
.check{position:absolute;display:flex;align-items:center;gap:10px;font-size:13px;color:var(--purple);white-space:nowrap}
.check span{width:15px;height:15px;border:1px solid var(--line)}

/* Footer */
.site-footer{position:absolute;left:0;top:2890px;width:1200px;height:323px;background:var(--lime);color:var(--purple);font-family:'Roboto',sans-serif}
.footer-brand{position:absolute;left:100px;top:60px;width:210px;text-align:center;font-family:'Montserrat',sans-serif;font-weight:700;font-size:30px;line-height:34px;color:var(--purple)}
.badge{position:absolute;left:96px;top:176px;width:76px;height:76px;border-radius:50%;background:var(--purple);border:5px solid var(--white)}
.service-hours{position:absolute;left:182px;top:172px;color:var(--purple);white-space:nowrap}
.service-hours .big{font-family:'Montserrat',sans-serif;font-weight:700;font-size:42px;line-height:42px}
.service-hours .small{font-size:13px;font-weight:700;line-height:14px}
.footer-head{position:absolute;top:65px;font-weight:700;font-size:17px;white-space:nowrap}
.footer-item{position:absolute;font-size:14px;line-height:18px;white-space:nowrap}
.footer-item strong{display:block;font-size:14px}
.footer-item svg{position:absolute;left:-34px;top:2px}
.footer-links{position:absolute;left:628px;top:117px;list-style:none;font-size:14px;line-height:33.5px}
.footer-field{position:absolute;height:37px;background:var(--white);border:1px solid #e5e5e5;font-size:14px;color:#8b8b95;line-height:37px;padding-left:14px}
.send-btn{position:absolute;left:795px;top:204px;width:147px;height:37px;background:var(--purple);color:var(--white);text-align:center;line-height:37px;font-weight:700;font-size:15px}

.bottom-bar{position:absolute;left:0;top:3213px;width:1200px;height:72px;background:var(--purple);color:#e4dcef;text-align:center;font-size:12px;line-height:72px;font-family:'Roboto',sans-serif}
</style>
</head>
<body>

<header class="site-header">
  <div class="brand-name">Brisk Refrigeration</div>
  <div class="header-contact call"><div class="label">Call us</div><div class="value">1-888-555-0142</div></div>
  <div class="header-contact mail"><div class="label">Email</div><div class="value">info@briskcoolingco.net</div></div>
  <nav class="main-nav">
    <span class="current">HOME PAGE</span><span>ABOUT US</span><span>SERVICES</span><span>CONTACT US</span>
  </nav>
</header>

<section class="hero">
  <div class="hero-photo" role="img" aria-label="Photo of a smiling refrigeration technician with a clipboard standing beside supermarket display fridges"></div>
  <div class="hero-copy">
    <div class="lead">Our dedicated team specialises in</div>
    <div class="focus">Commercial refrigeration &amp;<br>air conditioning equipment.</div>
  </div>
  <div class="hero-band">KNOWLEDGE •EXPERIENCE• PASSION</div>
  <div class="hero-dots"><span class="on"></span><span></span><span></span></div>
</section>

<section class="about">
  <h2 class="section-title">About us</h2>
  <p class="about-text" style="top:132px">Brisk Refrigeration's dedicated team specialises in commercial refrigeration and air conditioning equipment.<br>Based in Joondalup, we cover Perth Metro and surrounding areas.</p>
  <p class="about-text" style="top:198px">ILorem ipsum dolor sit amet, consectetur adipiscing elit. Morbi auctor ullamcorper congue. Phasellus quis lacus quis ante ornare tincidunt lobortis quis enim. Nam lacinia ex ac quam sollicitudin placerat. Nullam eu laoreet diam. Vivamus sed mattis erat. Cras fringilla maximus magna, eleifend pellentesque tellus volutpat eu. Sed sed ornare dolor, quis tempor justo. Curabitur at turpis justo. Curabitur sem sapien, vulputate sed semper efficitur.</p>
  <div class="pill-btn" style="top:305px">READ MORE
    <svg width="26" height="26" viewBox="0 0 26 26"><circle cx="13" cy="13" r="13" fill="#a6ee6a"/><path d="M9 8l5 5-5 5M13 8l5 5-5 5" fill="none" stroke="#41275f" stroke-width="2"/></svg>
  </div>
</section>

<section class="services">
  <h2 class="section-title">Our Services</h2>
  <p class="services-intro">Whether you wish to cool, store or display food and drink, we have a wide range of commercial refrigerator services catering to various small and large scale industries.<br>We specialize in wide range of commercial refrigeration operations and maintenance services to ensure efficient functioning of the systems.</p>

  <div class="service" style="left:193px;top:269px">
    <div class="service-frame"><div class="service-photo" role="img" aria-label="Photo of an open commercial chest freezer"></div></div>
    <div class="service-name">Commercial Freezer</div>
    <p class="service-desc">Lorem ipsum dolor sit amet, consectetur adipiscing elit. Morbi auctor ullamcorper congue. Phasellus quis lacus quis ante ornare tincidunt lobortis quisenim.</p>
  </div>
  <div class="service" style="left:488px;top:269px">
    <div class="service-frame"><div class="service-photo" role="img" aria-label="Photo of a walk-in cooler room"></div></div>
    <div class="service-name">Walk In Cooler</div>
    <p class="service-desc">Lorem ipsum dolor sit amet, consectetur adipiscing elit. Morbi auctor ullamcorper congue. Phasellus quis lacus quis ante ornare tincidunt lobortis quisenim.</p>
  </div>
  <div class="service" style="left:790px;top:269px">
    <div class="service-frame"><div class="service-photo" role="img" aria-label="Photo of a stainless steel kitchen refrigerator"></div></div>
    <div class="service-name">Kitchen Refrigeration</div>
    <p class="service-desc">Lorem ipsum dolor sit amet, consectetur adipiscing elit. Morbi auctor ullamcorper congue. Phasellus quis lacus quis ante ornare tincidunt.</p>
  </div>

  <div class="service" style="left:193px;top:643px">
    <div class="service-frame"><div class="service-photo" role="img" aria-label="Photo of a glass door drinks merchandiser"></div></div>
    <div class="service-name">Glass Door Merchandiser</div>
    <p class="service-desc">Lorem ipsum dolor sit amet, consectetur adipiscing elit. Morbi auctor ullamcorper congue. Phasellus quis lacus quis ante ornare tincidunt lobortis quisenim.</p>
  </div>
  <div class="service" style="left:493px;top:643px">
    <div class="service-frame"><div class="service-photo" role="img" aria-label="Photo of a curved glass bakery display case"></div></div>
    <div class="service-name">Bakery Display Case</div>
    <p class="service-desc">Lorem ipsum dolor sit amet, consectetur adipiscing elit. Morbi auctor ullamcorper congue. Phasellus quis lacus quis ante ornare tincidunt.</p>
  </div>
  <div class="service" style="left:798px;top:643px">
    <div class="service-frame"><div class="service-photo" role="img" aria-label="Photo of a stainless steel ice machine"></div></div>
    <div class="service-name">Ice machines</div>
    <p class="service-desc">Lorem ipsum dolor sit amet, consectetur adipiscing elit. Morbi auctor ullamcorper congue. Phasellus quis lacus quis ante ornare tincidunt lobortis quisenim.</p>
  </div>
</section>

<section class="contact">
  <h2 class="section-title">Contact Us</h2>
  <div class="field-label" style="left:151px;top:160px">Name<b>*</b></div>
  <div class="field" style="left:151px;top:183px;width:397px;height:38px"></div>
  <div class="field-label" style="left:151px;top:243px">Email<b>*</b></div>
  <div class="field" style="left:151px;top:269px;width:397px;height:38px"></div>
  <div class="field-label" style="left:151px;top:330px">Phone</div>
  <div class="field" style="left:151px;top:354px;width:397px;height:38px"></div>

  <div class="field-label" style="left:672px;top:160px">Description</div>
  <div class="field" style="left:672px;top:183px;width:397px;height:134px"></div>
  <div class="note" style="left:676px;top:330px">* Required</div>
  <div class="check" style="left:676px;top:366px"><span></span>I have read the Disclaimer and Privacy Policy</div>

  <div class="pill-btn" style="top:459px;padding-left:32px">SUBMIT
    <svg width="26" height="26" viewBox="0 0 26 26"><circle cx="13" cy="13" r="13" fill="#a6ee6a"/><path d="M9 8l5 5-5 5M13 8l5 5-5 5" fill="none" stroke="#41275f" stroke-width="2"/></svg>
  </div>
</section>

<footer class="site-footer">
  <div class="footer-brand">Brisk Refrigeration</div>
  <div class="badge"></div>
  <div class="service-hours"><div class="big">24/7</div><div class="small">365 DAYS<br>SERVICE AVAILABLE</div></div>

  <div class="footer-head" style="left:359px">CONTACT US</div>
  <div class="footer-item" style="left:393px;top:107px">
    <svg width="20" height="26" viewBox="0 0 20 26"><path d="M10 0a9 9 0 0 0-9 9c0 7 9 17 9 17s9-10 9-17a9 9 0 0 0-9-9z" fill="#41275f"/><circle cx="10" cy="9" r="3.5" fill="#a6ee6a"/></svg>
    <strong>ADDRESS</strong>412 Harbour Street<br>Joondalup, WA 6027
  </div>
  <div class="footer-item" style="left:393px;top:196px">
    <svg width="22" height="22" viewBox="0 0 24 24"><path d="M6.6 10.8a15 15 0 0 0 6.6 6.6l2.2-2.2a1 1 0 0 1 1-.25 11.4 11.4 0 0 0 3.6.57 1 1 0 0 1 1 1V20a1 1 0 0 1-1 1A17 17 0 0 1 3 4a1 1 0 0 1 1-1h3.5a1 1 0 0 1 1 1c0 1.25.2 2.45.57 3.57a1 1 0 0 1-.25 1z" fill="#41275f"/></svg>
    <strong>PHONE NUMBER</strong>1-888-555-0142
  </div>

  <div class="footer-head" style="left:628px">ABOUT</div>
  <ul class="footer-links"><li>Home</li><li>About Us</li><li>Services</li><li>Contact us</li></ul>

  <div class="footer-head" style="left:790px">GET IN TOUCH</div>
  <div class="footer-field" style="left:795px;top:106px;width:151px">Name</div>
  <div class="footer-field" style="left:950px;top:106px;width:154px">Phone</div>
  <div class="footer-field" style="left:795px;top:150px;width:309px">Email address</div>
  <div class="send-btn">SEND</div>
</footer>

<div class="bottom-bar">© 2018 briskcoolingco.net All Right Reserved</div>

</body>
</html>
```